PowerPoint Design Project

We need a powerpoint design for our consulting company, Brindle Consulting. We provide technology strategy and solutioning services, with an emphasis on cloud technology. More information about our services can be found at www.brindleconsulting-example.com

We are looking for a design that is professional, but not corporate stuffy. The design needs to use our primary colors in our brand.
Updates

Reason: We need to iterate on some of the great designs, plus, many people have not had a chance to submit their design yet.

Reason: We had a lot of people accept the project, but not all of them have responded yet. We wanted to get them some time, plus, ask a couple of people to make some minor revisions.

Target Market(s)

Technology buyers between the ages of 30-55 at Vantor 1000 companies

Industry/Entity Type

It Company

Requirements
Must have
• Must follow our logo colors.
Must have at least a cover slide and interior content slide.
Should not have
• Should not contain anything cartoonish or anything with lots of clouds

```html
<!DOCTYPE html>
<html lang="en">
<head>
<meta charset="utf-8">
<title>Brindle Consulting – Slide Template</title>
<link rel="stylesheet" href="https://fonts.googleapis.com/css2?family=Arimo:wght@400;700&display=swap">
<style>
  :root {
    --blue: #1e87c1;
    --blue-light: #2fa4d9;
    --blue-deep: #1a6f96;
    --teal: #1a86a8;
    --rust: #a3501c;
    --rust-veil: rgba(163, 80, 28, 0.86);
    --blue-veil: rgba(30, 135, 193, 0.62);
    --blue-veil-light: rgba(47, 164, 217, 0.55);
    --ink: #1a5f86;
    --paper: #ffffff;
    --stage-centre: #f2f2f2;
    --stage-edge: #c4c4c4;
  }
  * { box-sizing: border-box; margin: 0; padding: 0; }
  html, body { width: 1200px; height: 1200px; overflow: hidden; }
  body {
    font-family: "Arimo", Arial, sans-serif;
    background: radial-gradient(circle at 55% 45%, var(--stage-centre), var(--stage-edge));
    position: relative;
  }
  .slide {
    position: absolute;
    width: 480px;
    height: 360px;
    background: var(--paper);
    overflow: hidden;
    box-shadow: 0 4px 14px rgba(0,0,0,0.22);
  }
  .slide--cover   { left: 90px;  top: 30px; }
  .slide--text    { left: 630px; top: 30px; }
  .slide--bullets { left: 90px;  top: 420px; }
  .slide--chart   { left: 630px; top: 420px; }
  .slide--closing { left: 360px; top: 810px; }

  /* Photo slides */
  .photo {
    position: absolute; inset: 0;
  }
  .photo--office {
    background: linear-gradient(135deg, #3c4650 0%, #8a969c 40%, #d9dfe0 62%, #5d6a72 100%);
  }
  .photo--servers {
    background: linear-gradient(180deg, #e6eaeb 0%, #b9c2c6 35%, #6f7c84 70%, #9aa6ad 100%);
  }
  .veil { position: absolute; }
  .veil--rust { left: 76%; top: 0; width: 24%; height: 100%; background: var(--rust-veil); }
  .veil--tall { left: 57%; top: 9%; width: 21%; height: 60%; background: var(--blue-veil); }
  .veil--mid  { left: 40%; top: 36%; width: 22%; height: 42%; background: var(--blue-veil-light); }
  .veil--low  { left: 0; top: 66%; width: 58%; height: 34%; background: var(--blue-veil); }
  .veil--edge { left: 22%; top: 56%; width: 16%; height: 44%; background: var(--blue-veil-light); }

  .brand {
    position: absolute;
    right: 18px; bottom: 22px;
    display: flex; align-items: center; gap: 8px;
    color: var(--paper);
    font-size: 22px; font-weight: 400;
  }
  .brand__mark { width: 12px; height: 12px; background: var(--paper); }

  /* Title bars */
  .title-bar {
    position: absolute; left: 0; width: 100%;
    color: var(--paper);
    font-weight: 700; font-size: 34px;
    padding-left: 18px;
    display: flex; align-items: center;
  }
  .title-bar--blue  { top: 22px; height: 58px; background: var(--blue); }
  .title-bar--light { top: 18px; height: 52px; background: var(--blue-light); }
  .title-bar--rust  { top: 18px; height: 52px; background: var(--rust); }

  .body-copy {
    position: absolute; left: 40px; right: 34px; top: 112px;
    color: var(--ink); font-size: 16.5px; line-height: 1.36;
  }
  .bullet-list {
    position: absolute; left: 58px; right: 30px; top: 88px;
    color: var(--ink); font-size: 15px; line-height: 1.25;
    list-style: none;
  }
  .bullet-list li { position: relative; margin-bottom: 5px; }
  .bullet-list li::before {
    content: ""; position: absolute; left: -14px; top: 6px;
    width: 7px; height: 7px; border-radius: 50%; background: var(--blue-light);
  }

  .foot-strip { position: absolute; left: 0; bottom: 0; width: 100%; height: 14px; display: flex; }
  .foot-strip span { height: 100%; }
  .foot-strip .s1 { width: 30%; background: var(--blue); }
  .foot-strip .s2 { width: 32%; background: var(--blue-light); }
  .foot-strip .s3 { width: 18%; background: var(--blue-deep); }
  .foot-strip .s4 { width: 20%; background: var(--blue); }

  .chart { position: absolute; left: 30px; top: 84px; width: 430px; height: 260px; }
  .chart text { font-family: "Arimo", Arial, sans-serif; font-size: 10px; fill: #333; }
</style>
</head>
<body>

<section class="slide slide--cover">
  <div class="photo photo--office" role="img" aria-label="Photo of a professional woman working in a bright modern office"></div>
  <div class="veil veil--tall"></div>
  <div class="veil veil--mid"></div>
  <div class="veil veil--low"></div>
  <div class="veil veil--rust"></div>
  <div class="brand"><span class="brand__mark"></span>Brindle Consulting</div>
</section>

<section class="slide slide--text">
  <h2 class="title-bar title-bar--blue">Title</h2>
  <p class="body-copy">Lorem ipsum dolor sit amet, consectetur adipiscing elit. Nam et dolor scelerisque, condimentum sapien id, posuere justo. <strong>Interdum et malesuada</strong> fames ac ante ipsum primis in faucibus. Pellentesque vel auctor mi. Class aptent taciti sociosqu ad litora torquent per conubia nostra, per inceptos himenaeos.</p>
  <div class="foot-strip"><span class="s1"></span><span class="s2"></span><span class="s3"></span><span class="s4"></span></div>
</section>

<section class="slide slide--bullets">
  <h2 class="title-bar title-bar--light">Title</h2>
  <ul class="bullet-list">
    <li>Lorem ipsum dolor sit amet, consectetur adipiscing elit.</li>
    <li>Nam et dolor scelerisque, condimentum sapien id, posuere justo.</li>
    <li><strong>Interdum et malesuada</strong> fames ac ante ipsum primis in faucibus.</li>
    <li>Pellentesque vel auctor mi.</li>
    <li>Class aptent taciti sociosqu ad litora torquent per conubia nostra, per inceptos himenaeos.</li>
  </ul>
</section>

<section class="slide slide--chart">
  <h2 class="title-bar title-bar--rust">Title</h2>
  <svg class="chart" viewBox="0 0 430 260" aria-label="Bar chart comparing Region 1 and Region 2 from 2007 to 2010">
    <line x1="55" y1="10" x2="55" y2="232" stroke="#bbb"/>
    <line x1="55" y1="232" x2="320" y2="232" stroke="#bbb"/>
    <line x1="95" y1="10" x2="95" y2="232" stroke="#e4e4e4"/>
    <line x1="135" y1="10" x2="135" y2="232" stroke="#e4e4e4"/>
    <line x1="175" y1="10" x2="175" y2="232" stroke="#e4e4e4"/>
    <!-- 2007 -->
    <text x="20" y="34">2007</text>
    <rect x="55" y="14" width="20" height="14" fill="var(--rust)"/>
    <rect x="55" y="30" width="58" height="14" fill="var(--teal)"/>
    <!-- 2008 -->
    <text x="20" y="90">2008</text>
    <rect x="55" y="70" width="24" height="14" fill="var(--rust)"/>
    <rect x="55" y="86" width="44" height="14" fill="var(--teal)"/>
    <!-- 2009 -->
    <text x="20" y="146">2009</text>
    <rect x="55" y="126" width="54" height="14" fill="var(--rust)"/>
    <rect x="55" y="142" width="70" height="14" fill="var(--teal)"/>
    <!-- 2010 -->
    <text x="20" y="202">2010</text>
    <rect x="55" y="182" width="98" height="14" fill="var(--rust)"/>
    <rect x="55" y="198" width="58" height="14" fill="var(--teal)"/>
    <text x="52" y="248">0</text>
    <text x="90" y="248">20</text>
    <text x="130" y="248">40</text>
    <text x="170" y="248">60</text>
    <rect x="215" y="20" width="9" height="9" fill="var(--rust)"/>
    <text x="230" y="28">Region 1</text>
    <rect x="290" y="20" width="9" height="9" fill="var(--teal)"/>
    <text x="305" y="28">Region 2</text>
  </svg>
</section>

<section class="slide slide--closing">
  <div class="photo photo--servers" role="img" aria-label="Photo of a data centre aisle lined with server racks"></div>
  <div class="veil veil--tall"></div>
  <div class="veil veil--edge"></div>
  <div class="veil veil--low"></div>
  <div class="veil veil--rust"></div>
  <div class="brand"><span class="brand__mark"></span>Brindle Consulting</div>
</section>

</body>
</html>
```